Business Card and Simple Logo Desgin

New Zealand based start up company "Brook Advisory LTD" requires business cards and simple logo design.

Card Content.

Brook Advisory LTD

Joanna Pritchard
CA, BMS (Hons)

j.pritchard@brookadvisory.co.nz
PH +64 21 574 160

Target Market(s)

Corporate Business in IT, Finance and accounting.

Industry/Entity Type

Business

```html
<!DOCTYPE html>
<html lang="en">
<head>
<meta charset="utf-8">
<title>Brook Advisory LTD – Business Card</title>
<link href="https://fonts.googleapis.com/css2?family=Arimo:wght@700&family=Roboto+Condensed:wght@700&display=swap" rel="stylesheet">
<style>
  :root {
    --card-aqua: #9ffefd;
    --card-glow: #ffffff;
    --brand-blue: #00ccff;
    --accent-green: #5bc85b;
    --text-white: #ffffff;
    --page-bg: #ffffff;
  }
  html, body {
    margin: 0;
    padding: 0;
    width: 876px;
    height: 1200px;
    overflow: hidden;
    background: var(--page-bg);
  }
  .canvas {
    position: relative;
    width: 876px;
    height: 1200px;
  }
  .card {
    position: absolute;
    width: 866px;
    height: 561px;
    border-radius: 40px;
    overflow: hidden;
    font-family: "Arimo", Arial, sans-serif;
    font-weight: 700;
  }
  .card--front {
    left: 0;
    top: 0;
    background: var(--card-aqua);
  }
  .card--back {
    left: 7px;
    top: 637px;
    background: radial-gradient(circle at 50% 55%, var(--card-glow) 0%, #c8fffe 25%, var(--card-aqua) 75%);
  }
  .wave {
    position: absolute;
    inset: 0;
    width: 100%;
    height: 100%;
  }
  .brand {
    position: absolute;
    color: var(--brand-blue);
    line-height: 1;
  }
  .brand__name { display: block; }
  .brand--front {
    left: 60px;
    top: 70px;
  }
  .brand--front .brand__name { font-size: 92px; margin-left: 40px; }
  .brand--front .brand__tag { font-size: 38px; margin-top: 12px; display: block; }
  .brand--back {
    left: 0;
    right: 0;
    top: 235px;
    text-align: center;
  }
  .brand--back .brand__name { font-size: 150px; }
  .brand--back .brand__tag { font-size: 56px; margin-top: 16px; display: block; }
  .person {
    position: absolute;
    right: 25px;
    top: 272px;
    text-align: right;
    color: var(--accent-green);
    line-height: 1;
  }
  .person__name {
    font-size: 39px;
    letter-spacing: 3px;
    display: block;
  }
  .person__credentials {
    font-size: 27px;
    letter-spacing: 2px;
    display: block;
    margin-top: 4px;
  }
  .contact {
    position: absolute;
    left: 0;
    right: 0;
    top: 460px;
    text-align: center;
    color: var(--text-white);
    font-family: "Roboto Condensed", "Arial Narrow", sans-serif;
    font-size: 35px;
    line-height: 38px;
  }
  .contact span { display: block; }
</style>
</head>
<body>
<main class="canvas">
  <section class="card card--front">
    <svg class="wave" viewBox="0 0 866 561" aria-hidden="true">
      <path d="M0 390 C120 410 200 420 280 416 C420 405 520 355 650 354 C740 354 810 365 866 375 L866 561 L0 561 Z" fill="var(--brand-blue)"/>
      <path d="M0 390 C120 410 200 420 280 416 C420 405 520 355 650 354 C740 354 810 365 866 375" fill="none" stroke="var(--accent-green)" stroke-width="9"/>
    </svg>
    <div class="brand brand--front">
      <span class="brand__name">Brook</span>
      <span class="brand__tag">Advisory LTD</span>
    </div>
    <div class="person">
      <span class="person__name">Joanna Pritchard</span>
      <span class="person__credentials">CA, BMS (Hons)</span>
    </div>
    <div class="contact">
      <span class="contact__email">j.pritchard@brookadvisory.co.nz</span>
      <span class="contact__phone">PH +64 21 574 160</span>
    </div>
  </section>

  <section class="card card--back">
    <div class="brand brand--back">
      <span class="brand__name">Brook</span>
      <span class="brand__tag">Advisory LTD</span>
    </div>
  </section>
</main>
</body>
</html>
```